Automotive Accessories Business Card

Design a business template that match our new logo design and our industry.

https://www.kelvorauto.com/

Target Market(s)

Aftermarket auto parts and accessories

Industry/Entity Type

automotive

Contact Information for Business Card

company logo

Font styles to use
Serif
Sans Serif

Colors
EB3D1F
EC4F4E
F09395
F8D3D4
FCEDEE

```html
<!DOCTYPE html>
<html lang="en">
<head>
<meta charset="utf-8">
<title>Kelvor Auto Parts — Business Card</title>
<link rel="stylesheet" href="https://fonts.googleapis.com/css2?family=Arimo:wght@400;700&display=swap">
<style>
  :root {
    --bg: #e6e4e2;
    --red: #c4161f;
    --red-light: #d1252d;
    --charcoal: #38383a;
    --ink: #2b2b2b;
    --muted: #6a6a6a;
    --paper: #f7f7f5;
    --white: #ffffff;
  }
  * { box-sizing: border-box; margin: 0; padding: 0; }
  html, body { width: 1200px; height: 768px; overflow: hidden; }
  body {
    background: var(--bg);
    font-family: "Arimo", Arial, sans-serif;
    color: var(--ink);
    position: relative;
  }
  .card {
    position: absolute;
    top: 230px;
    width: 540px;
    height: 309px;
    box-shadow: 0 6px 18px rgba(0,0,0,0.18);
    overflow: hidden;
  }
  .card-back {
    left: 40px;
    background: linear-gradient(135deg, var(--red), var(--red-light));
    display: flex;
    align-items: center;
    justify-content: center;
  }
  .card-back .brand-name {
    color: var(--white);
    font-weight: 700;
    font-size: 44px;
    letter-spacing: 1px;
    text-transform: uppercase;
    text-align: center;
    line-height: 1.05;
  }
  .card-front {
    left: 620px;
    background: var(--paper);
  }
  .front-brand {
    position: absolute;
    left: 34px;
    top: 92px;
    width: 240px;
    display: flex;
    align-items: center;
    gap: 12px;
  }
  .brand-mark {
    width: 18px;
    height: 18px;
    background: var(--red);
    flex: none;
  }
  .front-brand .brand-name {
    color: var(--red);
    font-weight: 700;
    font-size: 30px;
    text-transform: uppercase;
    line-height: 1.05;
  }
  .divider {
    position: absolute;
    left: 292px;
    top: 34px;
    width: 1px;
    height: 190px;
    background: var(--muted);
  }
  .contact {
    position: absolute;
    left: 308px;
    top: 34px;
    width: 222px;
    font-size: 11.5px;
    line-height: 1.3;
    color: var(--ink);
  }
  .person-name {
    color: var(--red);
    font-weight: 700;
    font-size: 19px;
    text-transform: uppercase;
    letter-spacing: 0.5px;
  }
  .person-title { color: var(--muted); font-size: 11px; margin-bottom: 5px; }
  .office { margin-bottom: 6px; }
  .phone { display: flex; align-items: center; gap: 5px; }
  .phone svg { width: 10px; height: 10px; flex: none; }
  .email { margin-top: 2px; }
  .pattern-block {
    position: absolute;
    left: 22px;
    top: 240px;
    width: 66px;
    height: 30px;
    background: var(--red);
  }
  .web-band {
    position: absolute;
    left: 92px;
    top: 254px;
    right: 0;
    height: 24px;
    background: var(--charcoal);
    color: var(--white);
    font-size: 12px;
    display: flex;
    align-items: center;
    justify-content: flex-end;
    padding-right: 34px;
    letter-spacing: 0.3px;
  }
</style>
</head>
<body>
  <section class="card card-back">
    <div class="brand-name">Kelvor<br>Auto Parts</div>
  </section>

  <section class="card card-front">
    <div class="front-brand">
      <span class="brand-mark"></span>
      <div class="brand-name">Kelvor<br>Auto Parts</div>
    </div>

    <div class="divider"></div>

    <div class="contact">
      <div class="person-name">Daniel Moreno</div>
      <div class="person-title">Managing Director</div>
      <div class="office">
        240 W. Harbor Ave. Unit C<br>
        Riverton, CA, 92014<br>
        United States
        <div class="phone">
          <svg viewBox="0 0 10 10" aria-hidden="true"><path fill="#c4161f" d="M2.2 0.5 3.6 2.6 2.8 3.5C3.4 4.8 4.7 6.2 6.4 7.1L7.3 6.3 9.5 7.7 8.6 9.4C4.8 9.2 0.7 5.1 0.6 1.4Z"/></svg>
          1-800-555-0148
        </div>
      </div>
      <div class="office">
        5120 Maple Ridge Rd.<br>
        Surrey, BC V3W 2K7<br>
        Canada
        <div class="phone">
          <svg viewBox="0 0 10 10" aria-hidden="true"><path fill="#c4161f" d="M2.2 0.5 3.6 2.6 2.8 3.5C3.4 4.8 4.7 6.2 6.4 7.1L7.3 6.3 9.5 7.7 8.6 9.4C4.8 9.2 0.7 5.1 0.6 1.4Z"/></svg>
          604-555-0193
        </div>
      </div>
      <div class="email">sales@kelvorauto.com</div>
    </div>

    <div class="pattern-block" role="img" aria-label="Checkered racing flag pattern in red and charcoal"></div>
    <div class="web-band">www.kelvorauto.com</div>
  </section>
</body>
</html>
```